I own a rendering company which is in the construction industry i already have a logo i would like i

I want to make the website look professional and blends nicely with the logo, if i can have contact information and photos logos and a place where they can email me for job quotes or request and we want to win the big jobs so think also corporate in conjunction with construction. also an area for brief description and about us

Target Market(s)

Home owners/Investors, Small and major construction companies

Industry/Entity Type

Construction Company

Coding

Coded - Design and coding required

Number of Pages Required

3 page

Font styles to use
Serif
Sans Serif

Colors

Designer to choose colors to be used in the design.

Requirements
Must have
• An area for pictures to show with fade changes or clicking options(of white set walls, acrylic render expensive houses walls) an "about us" section. An area to where potential customers can email us (a writing box) where we can receive request for quotes and potential jobs. all contact information and license numbers
Nice to have
• pictures of plastered walls (posh elegant) and rendered walls acrylic and cement render
Should not have
• anything boring plain font etc

```html
<!DOCTYPE html>
<html lang="en">
<head>
<meta charset="utf-8">
<title>Kestrel Rendering</title>
<link href="https://fonts.googleapis.com/css2?family=Lato:wght@400;700;900&family=Roboto:wght@400;500;700&display=swap" rel="stylesheet">
<style>
:root{
  --red:#e51e25;
  --ink:#222222;
  --nav:#2e2e2e;
  --grey-bg:#efefef;
  --text:#6b6b6b;
  --dark-band:#2b2926;
  --footer:#121212;
  --footer-base:#0a0a0a;
  --field:#ededed;
  --white:#ffffff;
}
*{box-sizing:border-box;margin:0;padding:0}
html,body{width:1200px;height:3114px;overflow:hidden}
body{position:relative;background:var(--white);font-family:"Roboto",Arial,sans-serif;color:var(--ink)}
.abs{position:absolute}
.photo{position:absolute}

/* header */
.topbar{left:0;top:0;width:1200px;height:73px;background:var(--white)}
.call{right:80px;top:18px;display:flex;align-items:center;gap:14px;font-weight:700;font-size:19px}
.call .num{font-size:24px;font-weight:500}
.call-icon{width:46px;height:46px;border-radius:50%;background:var(--red);display:flex;align-items:center;justify-content:center}
.navbar{left:0;top:73px;width:1200px;height:62px;background:var(--nav)}
.nav{left:338px;top:73px;height:62px;display:flex}
.nav a{display:block;height:62px;line-height:62px;padding:0 30px;color:#ddd;text-decoration:none;font-size:16px;text-transform:uppercase}
.nav a.active{background:var(--red);color:var(--white);padding:0 28px}
.search{left:842px;top:82px;width:306px;height:44px;border:none;color:#ccc;font-size:14px;display:flex;align-items:center;justify-content:space-between;padding:0 0 0 18px}
.logo-box{left:77px;top:0;width:188px;height:156px;background:var(--white);box-shadow:0 2px 6px rgba(0,0,0,.25);display:flex;flex-direction:column;align-items:center;justify-content:center;z-index:3}
.logo-box .mark{width:30px;height:30px;border-radius:50%;background:var(--red);margin-bottom:10px}
.logo-box .name{font-weight:700;color:var(--red);font-size:25px;line-height:1.05;text-align:center;letter-spacing:.5px}

/* hero */
.hero-photo{left:0;top:135px;width:1200px;height:542px;background:linear-gradient(100deg,#8d857a 0%,#b3aa9c 35%,#cfcabf 60%,#bfb9ae 100%)}
.hero-title{right:80px;top:258px;width:620px;text-align:right;font-family:"Lato",Arial,sans-serif;font-weight:900;font-size:40px;line-height:50px;color:var(--white)}
.hero-text{right:80px;top:370px;width:560px;text-align:right;font-family:"Lato",Arial,sans-serif;font-size:14px;line-height:22px;color:var(--white)}
.btn{display:flex;align-items:center;justify-content:center;background:var(--red);color:var(--white);font-weight:500;text-transform:uppercase}
.hero-cta{left:847px;top:457px;width:275px;height:54px;font-size:20px}
.slide-arrow{width:52px;height:52px;border-radius:50%;background:rgba(30,30,30,.8);display:flex;align-items:center;justify-content:center}

/* service cards */
.card{top:619px;width:326px;height:380px;background:var(--white);text-align:center}
.card .pic{position:absolute;left:10px;top:8px;width:306px;height:198px}
.card h3{position:absolute;left:0;top:225px;width:100%;font-size:18px;font-weight:500;letter-spacing:.3px}
.card p{position:absolute;left:22px;top:258px;width:282px;font-size:13.5px;line-height:23px;color:#8a8a8a}
.card .arrow{position:absolute;left:147px;top:340px}

/* about */
.about-bg{left:0;top:1038px;width:1200px;height:523px;background:var(--grey-bg)}
.about-kicker{left:77px;top:1128px;font-size:20px;font-weight:500}
.about-title{left:77px;top:1158px;font-size:41px;color:var(--red);font-weight:500}
.about-p{left:77px;width:490px;font-size:13.5px;line-height:27px;color:var(--text)}
.about-btn{left:77px;top:1410px;width:176px;height:56px;font-size:19px}
.about-photo{left:623px;top:1115px;width:500px;height:374px;border:4px solid var(--white);display:flex}
.about-photo .half{flex:1;height:100%}

/* testimonials */
.testi{left:0;top:1561px;width:1200px;height:505px;background:radial-gradient(circle at 50% 50%,#36332f 0%,var(--dark-band) 70%)}
.testi-title{left:0;top:1624px;width:1200px;text-align:center;font-size:40px;color:var(--red)}
.avatar{left:540px;top:1695px;width:118px;height:118px;border-radius:50%;border:4px solid var(--white);background:linear-gradient(#c9c2b8,#8f867b)}
.quote{left:205px;top:1830px;width:790px;text-align:center;color:#d0d0d0;font-size:14.5px;line-height:29px}
.qmark{font-family:"Lato",serif;font-weight:900;font-size:52px;color:var(--red);line-height:1}
.client{left:0;top:1985px;width:1200px;text-align:center;color:var(--red);font-size:18px;font-weight:500}

/* quote form */
.worker{left:114px;top:2118px;width:374px;height:572px;background:linear-gradient(#d7d3cd,#6f7fa6 45%,#4a5f94 80%,#4b6189)}
.form-title{left:571px;top:2130px;font-size:41px;color:var(--red);font-weight:500}
.form-p{left:573px;top:2190px;width:520px;font-size:13.5px;line-height:26px;color:var(--text)}
.field{left:573px;width:540px;height:44px;background:var(--field);font-size:13.5px;color:#777;padding:12px 18px}
.submit{left:571px;top:2568px;width:176px;height:56px;font-size:19px}

/* email band */
.email-band{left:0;top:2690px;width:1200px;height:127px;background:var(--red)}
.email-title{left:77px;top:2716px;font-size:38px;color:var(--ink);font-weight:500}
.email-sub{left:77px;top:2764px;font-size:16px;color:var(--white)}
.email-input{left:397px;top:2726px;width:510px;height:56px;background:var(--white);font-size:14px;color:#444;display:flex;align-items:center;justify-content:space-between;padding:0 18px}
.subscribe{left:922px;top:2726px;width:166px;height:56px;border:2px solid var(--white);color:var(--white);font-size:20px;display:flex;align-items:center;justify-content:center}

/* footer */
.footer{left:0;top:2817px;width:1200px;height:235px;background:var(--footer)}
.f-col h4{font-size:16px;font-weight:500;color:var(--red);margin-bottom:16px}
.f-col ul{list-style:none}
.f-col li{font-size:14px;color:#cfcfcf;height:33px;padding-left:20px;position:relative}
.f-col li:before{content:"";position:absolute;left:0;top:6px;width:7px;height:7px;border-radius:50%;background:var(--red)}
.contact-row{display:flex;gap:16px;font-size:14px;color:#cfcfcf;line-height:24px;margin-bottom:12px}
.f-logo{left:930px;top:2838px;width:160px;text-align:center;color:var(--red);font-weight:700;font-size:28px;line-height:1.05}
.social{top:2976px;width:40px;height:40px;border-radius:50%;border:2px solid #777}
.social.on{background:var(--red);border-color:var(--red)}
.base{left:0;top:3052px;width:1200px;height:62px;background:var(--footer-base);color:#bbb;font-size:14px;text-align:center;line-height:62px}
</style>
</head>
<body>

<header>
  <div class="abs topbar"></div>
  <div class="abs call">Call Us On :
    <span class="call-icon"><svg width="22" height="22" viewBox="0 0 24 24"><path fill="#fff" d="M6.6 10.8c1.4 2.8 3.8 5.1 6.6 6.6l2.2-2.2c.3-.3.7-.4 1-.2 1.1.4 2.3.6 3.6.6.6 0 1 .4 1 1V20c0 .6-.4 1-1 1C10.6 21 3 13.4 3 4c0-.6.4-1 1-1h3.5c.6 0 1 .4 1 1 0 1.3.2 2.5.6 3.6.1.3 0 .7-.2 1z"/></svg></span>
    <span class="num">123 456 7890</span>
  </div>
  <div class="abs navbar"></div>
  <nav class="abs nav">
    <a class="active" href="#">Home</a><a href="#">About</a><a href="#">Services</a><a href="#">Contact</a>
  </nav>
  <div class="abs search">Search.....
    <svg width="20" height="20" viewBox="0 0 24 24"><circle cx="10" cy="10" r="6.5" fill="none" stroke="#ddd" stroke-width="2.5"/><path d="M15 15l6 6" stroke="#ddd" stroke-width="2.8"/></svg>
  </div>
  <div class="abs logo-box">
    <div class="mark"></div>
    <div class="name">KESTREL<br>RENDERING</div>
  </div>
</header>

<section class="hero">
  <div class="photo hero-photo" role="img" aria-label="Plasterer in a white shirt rendering a textured wall"></div>
  <h1 class="abs hero-title">Need A Acrylic And Cement Renderer ?</h1>
  <p class="abs hero-text">Lorem Ipsum is simply dummy text of the printing and typesetting industry. Lorem Ipsum has been the industry's standard dummy text ever since the, when an unknown printer.</p>
  <a class="abs btn hero-cta">Click to get quote</a>
  <div class="abs slide-arrow" style="left:12px;top:384px"><svg width="14" height="14" viewBox="0 0 14 14"><path d="M9 2L4 7l5 5" stroke="#fff" stroke-width="2" fill="none"/></svg></div>
  <div class="abs slide-arrow" style="left:1136px;top:384px"><svg width="14" height="14" viewBox="0 0 14 14"><path d="M5 2l5 5-5 5" stroke="#fff" stroke-width="2" fill="none"/></svg></div>
</section>

<section class="services">
  <article class="abs card" style="left:77px">
    <div class="pic" role="img" aria-label="Worker plastering a bright white wall" style="background:linear-gradient(135deg,#f4f4f4,#d9dde2)"></div>
    <h3>PLASTERED WALLS</h3>
    <p>Lorem Ipsum is simply dummy text of the printing and typesetting industry. Lorem Ipsum has been the..</p>
    <svg class="arrow" width="32" height="14" viewBox="0 0 32 14"><path d="M0 7h24" stroke="#e51e25" stroke-width="3"/><path d="M22 1l8 6-8 6z" fill="#e51e25"/></svg>
  </article>
  <article class="abs card" style="left:437px">
    <div class="pic" role="img" aria-label="Two workers applying acrylic render to a wall" style="background:linear-gradient(#c9ad8c,#b49573 70%,#3a3330)"></div>
    <h3>RENDERED WALLS ACRYLIC</h3>
    <p>Lorem Ipsum is simply dummy text of the printing and typesetting industry. Lorem Ipsum has been the..</p>
    <svg class="arrow" width="32" height="14" viewBox="0 0 32 14"><path d="M0 7h24" stroke="#e51e25" stroke-width="3"/><path d="M22 1l8 6-8 6z" fill="#e51e25"/></svg>
  </article>
  <article class="abs card" style="left:796px">
    <div class="pic" role="img" aria-label="Worker applying cement render over brickwork" style="background:linear-gradient(90deg,#9b5040,#a8927d 45%,#b8ada0)"></div>
    <h3>CEMENT RENDER</h3>
    <p>Lorem Ipsum is simply dummy text of the printing and typesetting industry. Lorem Ipsum has been the..</p>
    <svg class="arrow" width="32" height="14" viewBox="0 0 32 14"><path d="M0 7h24" stroke="#e51e25" stroke-width="3"/><path d="M22 1l8 6-8 6z" fill="#e51e25"/></svg>
  </article>
</section>

<section class="about">
  <div class="abs about-bg"></div>
  <svg class="abs" style="left:0;top:1038px" width="1200" height="523"><polygon points="785,523 1200,523 1200,7" fill="#e51e25"/></svg>
  <h4 class="abs about-kicker">ABOUT US</h4>
  <h2 class="abs about-title">KESTREL RENDERING</h2>
  <p class="abs about-p" style="top:1218px">Lorem Ipsum is simply dummy text of the printing and typesetting industry. has been the industry's standard dummy text ever.</p>
  <p class="abs about-p" style="top:1284px">Lorem Ipsum is simply dummy text of the printing and typesetting industry. has been the industry's standard dummy text ever since the, when an unknown printer Lorem Ipsum is simply dummy text of the printing and typesetting industry has been the industry's...</p>
  <a class="abs btn about-btn">Know more</a>
  <div class="abs about-photo">
    <div class="half" role="img" aria-label="Room before: peeling floral wallpaper" style="background:linear-gradient(90deg,#6b4a32,#c9b48e 40%,#e2d6bf)"></div>
    <div class="half" role="img" aria-label="Room after: freshly plastered white walls" style="background:linear-gradient(#f6f6f4,#e6e6e2 80%,#6a4a38)"></div>
  </div>
  <div class="abs slide-arrow" style="left:614px;top:1275px;width:32px;height:56px;border-radius:0 28px 28px 0;background:rgba(40,40,40,.75)"><svg width="12" height="14" viewBox="0 0 12 14"><path d="M8 2L3 7l5 5" stroke="#fff" stroke-width="2" fill="none"/></svg></div>
  <div class="abs slide-arrow" style="left:1092px;top:1275px;width:32px;height:56px;border-radius:28px 0 0 28px;background:rgba(40,40,40,.75)"><svg width="12" height="14" viewBox="0 0 12 14"><path d="M4 2l5 5-5 5" stroke="#fff" stroke-width="2" fill="none"/></svg></div>
</section>

<section class="testimonials">
  <div class="abs testi"></div>
  <h2 class="abs testi-title">WHAT OUR CLIENT SAY</h2>
  <div class="abs avatar" role="img" aria-label="Client portrait"></div>
  <span class="abs qmark" style="left:166px;top:1826px">&ldquo;</span>
  <p class="abs quote">Lorem Ipsum is simply dummy text of the printing and typesetting industry. Lorem Ipsum has been the industry's standard dummy text ever since the 1500s, when an unknown printer took a galley of type and scrambled it to make Lorem Ipsum is simply dummy text of the printing Lorem Ipsum is simply dummy text..</p>
  <span class="abs qmark" style="left:985px;top:1890px">&rdquo;</span>
  <svg class="abs" style="left:238px;top:1930px" width="740" height="30"><line x1="0" y1="8" x2="740" y2="8" stroke="#e51e25" stroke-width="1.5" stroke-dasharray="5 4"/><path d="M340 8l12 14 12-14" fill="#2b2926" stroke="#e51e25" stroke-width="1.5"/></svg>
  <div class="abs client">CLIENT NAME</div>
  <svg class="abs" style="left:28px;top:1796px" width="20" height="44"><path d="M16 2L4 22l12 20" stroke="#888" stroke-width="2" fill="none"/></svg>
  <svg class="abs" style="left:1152px;top:1796px" width="20" height="44"><path d="M4 2l12 20-12 20" stroke="#888" stroke-width="2" fill="none"/></svg>
</section>

<section class="quote-form">
  <div class="photo worker" role="img" aria-label="Smiling tradesman in cap and work shirt holding a clipboard"></div>
  <h2 class="abs form-title">GET A FREE QUOTE</h2>
  <p class="abs form-p">Lorem Ipsum is simply dummy text of the printing and typesetting industry. has been the industry's standard dummy text ever.</p>
  <div class="abs field" style="top:2255px">Name *</div>
  <div class="abs field" style="top:2307px">Email *</div>
  <div class="abs field" style="top:2359px">Phone *</div>
  <div class="abs field" style="top:2411px">Services *</div>
  <div class="abs field" style="top:2464px;height:94px">Message *</div>
  <a class="abs btn submit">Submit</a>
</section>

<section class="newsletter">
  <div class="abs email-band"></div>
  <h2 class="abs email-title">EMAIL ME</h2>
  <p class="abs email-sub">You have any questions Keep in Touch</p>
  <div class="abs email-input">Enter Your Email
    <svg width="22" height="18" viewBox="0 0 22 18"><rect x="2" y="3" width="17" height="12" fill="none" stroke="#e51e25" stroke-width="2" transform="rotate(-12 11 9)"/><path d="M3 4l8 6 8-7" fill="none" stroke="#e51e25" stroke-width="2"/></svg>
  </div>
  <div class="abs subscribe">SUBSCRIBE</div>
</section>

<footer>
  <div class="abs footer"></div>
  <div class="abs f-col" style="left:77px;top:2842px">
    <h4>SITEMAP</h4>
    <ul><li>Home</li><li>About Us</li><li>Services</li><li>Contact Us</li></ul>
  </div>
  <div class="abs f-col" style="left:345px;top:2842px">
    <h4>SERVICES</h4>
    <ul><li>Plastered Walls</li><li>Rendered Walls Acrylic</li><li>Cement Render</li></ul>
  </div>
  <div class="abs f-col" style="left:608px;top:2842px;width:290px">
    <h4>CONTACT US</h4>
    <div class="contact-row"><svg width="14" height="20" viewBox="0 0 14 20"><path d="M7 0a7 7 0 0 0-7 7c0 5 7 13 7 13s7-8 7-13a7 7 0 0 0-7-7z" fill="#e51e25"/><circle cx="7" cy="7" r="2.5" fill="#121212"/></svg><span>101 - Lorem Ipsum is simple<br>dummy text of print text</span></div>
    <div class="contact-row"><svg width="16" height="14" viewBox="0 0 16 14"><rect y="1" width="16" height="12" fill="#e51e25"/><path d="M0 1l8 6 8-6" stroke="#121212" stroke-width="1.5" fill="none"/></svg><span>info@kestrelrendering.com</span></div>
    <div class="contact-row"><svg width="16" height="16" viewBox="0 0 24 24"><path fill="#e51e25" d="M6.6 10.8c1.4 2.8 3.8 5.1 6.6 6.6l2.2-2.2c.3-.3.7-.4 1-.2 1.1.4 2.3.6 3.6.6.6 0 1 .4 1 1V20c0 .6-.4 1-1 1C10.6 21 3 13.4 3 4c0-.6.4-1 1-1h3.5c.6 0 1 .4 1 1 0 1.3.2 2.5.6 3.6.1.3 0 .7-.2 1z"/></svg><span>(555)014-2277</span></div>
  </div>
  <div class="abs f-logo">KESTREL<br>RENDERING</div>
  <div class="abs social on" style="left:935px"></div>
  <div class="abs social" style="left:985px"></div>
  <div class="abs social" style="left:1035px"></div>
  <div class="abs base">&copy;KESTREL RENDERING - 2017 All Right Reserved.</div>
</footer>

</body>
</html>
```